依頼概要
■依頼の目的/概要
弊社ではあささんぽ、あさひを浴びようと思えるSNSアプリの制作を行っております。
そよかぜてちょうアプリでは毎日の記録をつけるためのライフログ系の機能を制作しております。

ライフログとして自分の記録を見返したり、他のユーザーからも見てもらえる機能がある日記のデザイン及びその画面のUI制作をお願いします。

■依頼の詳細
ユーザーが投稿するのは朝日を含めた毎朝の日記で自分のそよかぜてちょう(本のテイスト)の左ページを投稿します(アプリ上ホーム画面)。その日記投稿や朝散歩をすればするほど幸せの証として「そよかぜスター」を報酬として獲得し、毎朝獲得したハートを自分のそよかぜてちょうの右ページに貯めておけます(アプリ上そよかぜてちょう画面)。

今回トライアルでお願いしたいのはユーザーが朝日を投稿するホーム画面のUIです(左ページ)。
必要な要項といたしましては、
・ユーザーが撮影した朝日の写真(必須)
・日付(必須)
・天気※
・場所※
・気温※
・日記コメント※
・自分のキャラクター(こちらは素材があります)※

を入れられるようにしたいと考えております。
※は、ユーザー任意で入れたり、非表示にできます

スワイプすると、他のユーザーの日記のページをめくるような感覚のモーションの検討もしています。

こちらをトライアルという形で、採用された方には別画面/別バージョンの本のデザインや詳細なUIなどご相談したいと考えております。追加のUIのお見積りなども含め、ご提案いただけますと幸いです。

現在の開発中の仮デザインを添付しますが、よりよいデザインを是非、応募いただけますと幸いです。

画面UIのデザインがイメージと合っていた為。

この度、ご提案いただきありがとうございました。ご厚情にお応えすることができず、誠に申し訳ございません。勝手ではございますが、これに懲りず今後ともお付き合いくださいますようお願い申し上げます。

```html
<!DOCTYPE html>
<html lang="ja">
<head>
<meta charset="UTF-8">
<title>そよかぜてちょう ホーム</title>
<link rel="stylesheet" href="https://fonts.googleapis.com/css2?family=Noto+Sans+JP:wght@400;500;700&family=Roboto:wght@500;700&display=swap">
<style>
  :root {
    --bg: #eef0f0;
    --bg-shade: #dde2e2;
    --cover: #4d6f6d;
    --page: #ffffff;
    --page-edge: #e6e9e9;
    --tab: #a8d84e;
    --ink: #333a3a;
    --ink-soft: #5e6666;
    --sun: #ec6a5e;
    --teal: #2f5b5c;
    --pin: #5b9c96;
    --rule: #c9cfcf;
    --photo-sky: #c9bfa8;
    --photo-mid: #a8977a;
    --photo-ground: #33402a;
  }
  * { margin: 0; padding: 0; box-sizing: border-box; }
  html, body { width: 1200px; height: 2184px; overflow: hidden; }
  body {
    background: linear-gradient(125deg, var(--bg) 0%, var(--bg) 55%, var(--bg-shade) 100%);
    font-family: "Noto Sans JP", sans-serif;
    color: var(--ink);
    position: relative;
  }
  .tab {
    position: absolute;
    left: 180px; top: 120px;
    width: 200px; height: 108px;
    background: var(--tab);
    border-radius: 4px 4px 0 0;
  }
  .notebook {
    position: absolute;
    left: 44px; top: 204px;
    width: 1152px; height: 1956px;
    background: var(--cover);
    border-radius: 28px 10px 10px 28px;
    box-shadow: 0 18px 40px rgba(40,60,60,0.18);
  }
  .page-stack {
    position: absolute;
    left: 72px; top: 200px;
    width: 1112px; height: 1924px;
    background: var(--page-edge);
    border-radius: 4px 14px 14px 4px;
  }
  .page {
    position: absolute;
    left: 72px; top: 200px;
    width: 1100px; height: 1916px;
    background: var(--page);
    border-radius: 4px 12px 12px 4px;
    box-shadow: inset 18px 0 24px -18px rgba(0,0,0,0.15);
  }
  .date-year {
    position: absolute; left: 144px; top: 284px;
    font-family: "Roboto", sans-serif; font-weight: 500;
    font-size: 38px; color: var(--ink);
  }
  .date-day {
    position: absolute; left: 140px; top: 322px;
    font-family: "Roboto", sans-serif; font-weight: 700;
    font-size: 104px; line-height: 1; color: var(--ink);
    letter-spacing: -2px; white-space: nowrap;
  }
  .date-day .slash { font-weight: 500; color: var(--ink-soft); }
  .date-day .weekday {
    font-family: "Noto Sans JP", sans-serif; font-weight: 500;
    font-size: 36px; letter-spacing: 0; margin-left: 10px;
  }
  .meta {
    position: absolute; top: 344px; left: 492px;
    display: flex; align-items: center; height: 80px;
    font-size: 44px; font-weight: 500; white-space: nowrap;
  }
  .meta svg { width: 80px; height: 80px; flex: none; }
  .meta .weather-label { margin-left: 22px; }
  .meta .divider { width: 2px; height: 30px; background: var(--rule); margin: 0 62px 0 72px; }
  .meta .temp-label { margin-left: 22px; font-family: "Roboto", "Noto Sans JP", sans-serif; font-weight: 500; }
  .photo {
    position: absolute; left: 148px; top: 466px;
    width: 920px; height: 686px; border-radius: 16px;
    background: linear-gradient(180deg, var(--photo-sky) 0%, var(--photo-mid) 50%, var(--photo-ground) 100%);
  }
  .location {
    position: absolute; left: 150px; top: 1168px;
    display: flex; align-items: center; gap: 12px;
    font-size: 38px; color: var(--ink-soft);
  }
  .location svg { width: 30px; height: 40px; }
  .entry {
    position: absolute; left: 148px; top: 1276px;
    font-size: 48px; line-height: 86px; letter-spacing: 1px;
    color: var(--ink);
  }
  .entry .line { display: block; white-space: nowrap; }
</style>
</head>
<body>
  <div class="tab"></div>
  <div class="notebook"></div>
  <div class="page-stack"></div>
  <main class="page"></main>

  <div class="date-year">2023</div>
  <div class="date-day">3<span class="slash">/</span>22<span class="weekday">水</span></div>

  <div class="meta">
    <svg viewBox="0 0 80 80" aria-hidden="true">
      <circle cx="40" cy="40" r="40" fill="var(--sun)"/>
      <circle cx="40" cy="40" r="11" fill="none" stroke="#fff" stroke-width="4"/>
      <g stroke="#fff" stroke-width="4" stroke-linecap="round">
        <line x1="40" y1="16" x2="40" y2="22"/><line x1="40" y1="58" x2="40" y2="64"/>
        <line x1="16" y1="40" x2="22" y2="40"/><line x1="58" y1="40" x2="64" y2="40"/>
        <line x1="23" y1="23" x2="27" y2="27"/><line x1="53" y1="53" x2="57" y2="57"/>
        <line x1="57" y1="23" x2="53" y2="27"/><line x1="27" y1="53" x2="23" y2="57"/>
      </g>
    </svg>
    <span class="weather-label">晴れ</span>
    <span class="divider"></span>
    <svg viewBox="0 0 80 80" aria-hidden="true">
      <circle cx="40" cy="40" r="40" fill="var(--teal)"/>
      <rect x="34" y="16" width="12" height="32" rx="6" fill="none" stroke="#fff" stroke-width="4"/>
      <circle cx="40" cy="54" r="10" fill="none" stroke="#fff" stroke-width="4"/>
      <line x1="40" y1="30" x2="40" y2="54" stroke="#fff" stroke-width="4" stroke-linecap="round"/>
    </svg>
    <span class="temp-label">20℃</span>
  </div>

  <div class="photo" role="img" aria-label="ユーザーが撮影した朝日の写真"></div>

  <div class="location">
    <svg viewBox="0 0 30 40" aria-hidden="true">
      <path d="M15 2C8 2 3 7 3 14c0 9 12 23 12 23s12-14 12-23C27 7 22 2 15 2z" fill="var(--pin)"/>
      <circle cx="15" cy="14" r="5" fill="#fff"/>
    </svg>
    <span>匿名県岳師山</span>
  </div>

  <p class="entry">
    <span class="line">朝起きて布団から出るのが辛かった。昨晩</span>
    <span class="line">は遅くまで起きていたせいか、目が覚めて</span>
    <span class="line">もまだ眠かった。でも今日は快晴で早く</span>
    <span class="line">起きて準備をして外に出かけた。やはり早</span>
    <span class="line">朝の気持ちいい空気を吸うと気分がすっき</span>
    <span class="line">りする。</span>
  </p>
</body>
</html>
```